WordPress Design for both website and landing page for an expert

I need a clean and stylish design for my new website. I work as an expert (see attached file WHY HOW WHAT), my product is expert opinion (reports) for company evaluations You can use all of the attached pictures colored or black / white. The person is me, you can add other pictures, if you want. The design should be clean and stylish, so you could use white, black, gray, silver and / or one additional color. I have added an idea about my website, see attached file CONCEPT WEBSITE If you have any more information, please do not hesitate to contact us 'Hesitate to ask me ...

```html
<!DOCTYPE html>
<html lang="de">
<head>
<meta charset="utf-8">
<title>Lukas Brandt – Sachverständiger für Firmenbewertungen</title>
<link rel="stylesheet" href="https://fonts.googleapis.com/css2?family=Catamaran:wght@500;600;700;800&family=Lato:wght@400;700&display=swap">
<style>
  :root {
    --white: #ffffff;
    --ink: #111111;
    --heading-grey: #5a5a5a;
    --text-grey: #666666;
    --body: #222222;
    --navy: #1f2d4d;
    --icon-grey: #aeb6bc;
    --icon-dark: #6f6f6f;
    --faint: #e3e3e3;
    --pill-bg: #efefef;
    --pill-border: #dcdcdc;
    --footer: #3b3b3b;
    --band: rgba(70, 70, 70, 0.82);
  }
  * { margin: 0; padding: 0; box-sizing: border-box; }
  html, body { width: 1200px; height: 2324px; overflow: hidden; background: var(--white); }
  body { position: relative; font-family: "Lato", sans-serif; color: var(--body); }

  /* Hero */
  .hero {
    position: absolute; left: 0; top: 0; width: 1200px; height: 675px;
    background: linear-gradient(160deg, #4a4a4a 0%, #8a8580 22%, #d9d6d2 48%, #eceae8 70%, #b9b6b2 100%);
  }
  .brand {
    position: absolute; left: 100px; top: 96px; width: 256px; white-space: nowrap;
    font-family: "Catamaran", sans-serif; font-weight: 500; font-size: 23px; line-height: 1;
    letter-spacing: 4px; color: var(--white); text-transform: uppercase; text-align: center;
  }
  .nav { position: absolute; top: 65px; left: 516px; display: flex; gap: 33px; }
  .nav a {
    font-family: "Lato", sans-serif; font-size: 14px; color: var(--white);
    text-decoration: none; text-transform: uppercase; position: relative; white-space: nowrap;
  }
  .nav a.is-active { font-weight: 700; }
  .nav a.is-active::after {
    content: ""; position: absolute; left: 0; top: 21px; width: 22px; height: 3px; background: var(--white);
  }
  .hero-band {
    position: absolute; left: 0; top: 557px; width: 1200px; height: 118px;
    background: var(--band); text-align: center; color: var(--white);
  }
  .hero-title { font-family: "Catamaran", sans-serif; font-weight: 700; font-size: 38px; margin-top: 16px; line-height: 1.1; }
  .hero-sub { font-family: "Catamaran", sans-serif; font-weight: 500; font-size: 21px; margin-top: 6px; letter-spacing: .3px; }

  /* Reasons */
  .section-mark {
    position: absolute; left: 0; width: 1200px; text-align: center; top: 760px;
    font-family: "Catamaran", sans-serif; font-weight: 700; font-size: 24px; letter-spacing: 4px; color: var(--faint);
  }
  .section-title {
    position: absolute; left: 0; top: 812px; width: 1200px; text-align: center;
    font-family: "Catamaran", sans-serif; font-weight: 800; font-size: 34px; letter-spacing: 1.5px; color: var(--heading-grey);
  }
  .reason { position: absolute; top: 923px; width: 270px; text-align: center; }
  .reason-icon {
    display: block; margin: 0 auto; width: 270px; height: 136px; border-radius: 68px;
    background: radial-gradient(ellipse at center, #eef0f1 0%, #d8dde0 55%, var(--icon-grey) 100%);
  }
  .reason-title {
    font-family: "Catamaran", sans-serif; font-weight: 700; font-size: 28px; color: var(--heading-grey);
    margin-top: 46px; line-height: 1;
  }
  .reason-text { font-size: 13.5px; line-height: 22px; color: var(--ink); margin-top: 14px; }

  /* Promise */
  .promise {
    position: absolute; left: 0; top: 1297px; width: 1200px; height: 487px;
    background: linear-gradient(90deg, #d3d2cf 0%, #dcdbd8 40%, #d9d7d4 55%);
  }
  .promise-portrait {
    position: absolute; right: 0; top: 0; width: 600px; height: 487px;
    background:
      radial-gradient(ellipse 120px 150px at 380px 150px, #d6b7a4 0%, rgba(214,183,164,0) 100%),
      radial-gradient(ellipse 220px 260px at 420px 320px, #f7f7f6 0%, rgba(247,247,246,0) 100%),
      linear-gradient(90deg, rgba(217,215,212,0) 0%, #cfc8c2 30%, #c79b80 75%, #b5785a 100%);
  }
  .promise-mark {
    position: absolute; left: 123px; top: 125px; width: 440px; text-align: center;
    font-family: "Catamaran", sans-serif; font-weight: 800; font-size: 56px; letter-spacing: 6px; color: rgba(150,150,150,.55);
  }
  .promise-title {
    position: absolute; left: 103px; top: 242px; width: 480px; text-align: center;
    font-family: "Catamaran", sans-serif; font-weight: 800; font-size: 36px; color: var(--ink); letter-spacing: .5px;
  }
  .promise-text {
    position: absolute; left: 118px; top: 300px; width: 450px; text-align: center;
    font-size: 23px; line-height: 40.5px; color: var(--ink);
  }

  /* Questions */
  .questions { position: absolute; top: 1852px; list-style: none; }
  .questions li {
    position: relative; padding-left: 36px; font-size: 15.3px; line-height: 21px; color: var(--navy); margin-bottom: 21px;
  }
  .questions li::before {
    content: ""; position: absolute; left: 0; top: 6px; width: 10px; height: 10px; border-radius: 50%; background: var(--icon-grey);
  }
  .divider { position: absolute; left: 600px; top: 1858px; width: 1px; height: 152px; background: #cfcfcf; }

  .pill {
    position: absolute; left: 126px; top: 2073px; width: 947px; height: 76px;
    background: var(--pill-bg); border: 1px solid var(--pill-border); border-radius: 38px;
    text-align: center; font-size: 19px; line-height: 26px; color: var(--text-grey); padding-top: 11px;
  }
  .note {
    position: absolute; left: 160px; top: 2166px; width: 880px; text-align: center;
    font-size: 14.5px; line-height: 24px; color: var(--text-grey);
  }
  .note strong { color: #333; }

  .footer {
    position: absolute; left: 0; top: 2287px; width: 1200px; height: 37px; background: var(--footer);
    color: var(--white); font-size: 12.6px; text-align: center; line-height: 37px;
  }
</style>
</head>
<body>

<header class="hero" role="img" aria-label="Photo: a person writing on printed bar charts with a pen beside a laptop">
  <div class="brand">Lukas Brandt</div>
  <nav class="nav">
    <a class="is-active" href="#">Home</a>
    <a href="#">What I do</a>
    <a href="#">Why I do it &amp; how I do it</a>
    <a href="#">About me</a>
    <a href="#">Contact</a>
  </nav>
  <div class="hero-band">
    <h1 class="hero-title">Sachverständiger für Firmenbewertungen</h1>
    <p class="hero-sub">Sie benötigen ein Gutachten zur Ermittlung des Wertes Ihres Unternehmens</p>
  </div>
</header>

<div class="section-mark">Lukas Brandt</div>
<h2 class="section-title">WHY YOU SHOULD WORK WITH ME</h2>

<section class="reason" style="left:119px">
  <div class="reason-icon" role="img" aria-label="Icon illustration: running figure standing for speed"></div>
  <h3 class="reason-title">Schnell</h3>
  <p class="reason-text">Sie bekommen Ihr Gutachten zeitnah (innerhalb von max. 21 Tagen nach Zugang aller benötigten Unterlagen)</p>
</section>

<section class="reason" style="left:465px">
  <div class="reason-icon" role="img" aria-label="Icon illustration: certificate with seal"></div>
  <h3 class="reason-title">Zertifiziert</h3>
  <p class="reason-text">Sie erhalten ein qualifiziertes und belastbares Gutachten von einem zertifizierten Sachverständigen (höchste Akzeptanz bei allen Parteien)</p>
</section>

<section class="reason" style="left:810px">
  <div class="reason-icon" role="img" aria-label="Icon illustration: person balancing two weights"></div>
  <h3 class="reason-title">Verständlich</h3>
  <p class="reason-text">Ihr Gutachten wird für Sie logisch und nachvollziehbar sein und kein “Fachchinesisch” enthalten</p>
</section>

<section class="promise">
  <div class="promise-portrait" role="img" aria-label="Photo: the expert in a white shirt leaning on a railing in a bright interior with warm orange tones"></div>
  <div class="promise-mark">Lukas Brandt</div>
  <h2 class="promise-title">MY QUALITY PROMISE :</h2>
  <p class="promise-text">should the advised date for the preparation of the report be exceeded, you will receive the report free of chare (I waive my fee)</p>
</section>

<ul class="questions" style="left:121px; width:460px">
  <li>What are the buying motives of the customers?</li>
  <li>Sie wollen Anteile Ihres Unternehmens oder ihr gesamtes Unternehmen verkaufen?</li>
  <li>Sie müssen im Rahmen einer Trennung/Scheidung jemanden ausbezahlen und benötigen eine Bemessungsgrundlage?</li>
</ul>
<div class="divider"></div>
<ul class="questions" style="left:660px; width:420px">
  <li>Was sind die Kaufmotive der Kunden?</li>
  <li>Sie wollen Ihr Unternehmen auf Ihre Erben übertragen<br>und benötigen eine Bewertung für das Finanzamt?</li>
</ul>

<div class="pill">Lassen Sie Ihr Unternehmen von einem qualifizerten Sachverständigen bewerten und gehen somit<br>vielen (unnötigen) Streitereien aus dem Weg.</div>
<p class="note"><strong>Merke</strong>: Die Kosten für ein Gutachten sind immer überproportional günstiger als die Kosten für Rechtsstreitigkeiten. Und das losgelöst<br>von der psychischen Belastung einer solchen Auseinandersetzung ...</p>

<footer class="footer">© 2019 by Lukas Brandt. All right reserved.</footer>

</body>
</html>
```